Fast Money - Simple Book Cover Design

Hello,

I am in need of a cover for my new book. The Book Title Is

"Standing Growth - Keys to Glowing Customer Ratings That Fill The Calendar and Draw Fresh Clients Through Every Entrance!"

Author: Fireman Dale Orsworth

What I want: This is a book for businesses on improving their online reputation. I want to have 5 Stars on the cover. You can look at this quarvex search for ideas of what I am meaning.....

(copy and paste)

http://www.quarvex-find.example/search?q=5+star+online+reviews&mode=images&ref=kx7Lp2QwZt9 (copy and paste)

I am open to different color schemes for the book. I am partial to dark blues if you make it look good. Here is another book that I really like the cover of....

http://www.brindlemart.example/Clipwave-Tactics-Earning-Promotion-ebook/item/Z93KT4WQPX

I want the cover BOLD and to STAND OUT.

I am looking for a design to help establish me as an authority for online reputation marketing. This book will be both in Pagely format and be used in print as well.

I am open to questions....

Thanks!

Dale

Reason: I don't believe we have received the right designs. I am going to give everyone more time...

Reason: Hi everyone, I had some stuff come up and was not able to be involved in this project. I am extending because we have not seen the exact thing we want and need time to work with designers to get it right. Thanks Dale

Reason: I am currently traveling and can't wrap this up until I get back.

Target Market(s)

Business Owners

Industry/Entity Type

Business

Requirements
Must have
• Title and Subtitle

Author Name

5 Stars Images....
Nice to have
• Creativity

Bold and stand out

Professional

Should not have
• thin text, small to read text, lame graphics,

```html
<!DOCTYPE html>
<html lang="en">
<head>
<meta charset="UTF-8">
<title>Standing Growth – Book Cover</title>
<link rel="stylesheet" href="https://fonts.googleapis.com/css2?family=Arimo:wght@700&display=swap">
<style>
  :root {
    --band-1: #2f4b5b;
    --band-2: #2d6f8e;
    --band-3: #2793ab;
    --band-4: #5aa6b6;
    --band-5: #efb43c;
    --title-white: #ffffff;
    --author-gold: #f2b13a;
    --star-light: #ffe680;
    --star-mid: #f7c42c;
    --star-dark: #d9921a;
    --text-shadow: rgba(0, 0, 0, 0.45);
  }
  html, body {
    margin: 0;
    padding: 0;
    width: 900px;
    height: 1200px;
    overflow: hidden;
    background: #ffffff;
  }
  .cover {
    position: relative;
    width: 900px;
    height: 1200px;
    overflow: hidden;
    font-family: "Arimo", Arial, Helvetica, sans-serif;
    font-weight: 700;
  }
  .bands {
    position: absolute;
    inset: 0;
    display: flex;
  }
  .band {
    flex: 1;
    background-image: linear-gradient(180deg, rgba(255,255,255,0.06), rgba(0,0,0,0.04));
  }
  .band--1 { background-color: var(--band-1); }
  .band--2 { background-color: var(--band-2); }
  .band--3 { background-color: var(--band-3); }
  .band--4 { background-color: var(--band-4); }
  .band--5 { background-color: var(--band-5); }

  .backdrop-photo {
    position: absolute;
    left: 0;
    top: 0;
    width: 900px;
    height: 900px;
    background:
      radial-gradient(ellipse 300px 140px at 420px 640px, rgba(255,255,255,0.16), rgba(255,255,255,0) 70%),
      radial-gradient(ellipse 520px 420px at 360px 420px, rgba(255,255,255,0.08), rgba(255,255,255,0) 75%);
  }

  .author {
    position: absolute;
    left: 56px;
    top: 128px;
    height: 824px;
    margin: 0;
    writing-mode: vertical-rl;
    transform: rotate(180deg);
    font-size: 62px;
    line-height: 1;
    color: var(--author-gold);
    letter-spacing: 0.5px;
    white-space: nowrap;
    text-align: center;
    text-shadow: 0 2px 4px rgba(0,0,0,0.25);
  }

  .title-block {
    position: absolute;
    right: 45px;
    top: 72px;
    text-align: right;
    color: var(--title-white);
  }
  .title {
    margin: 0;
    font-size: 106px;
    line-height: 0.86;
    letter-spacing: -1px;
    text-shadow: 3px 4px 6px var(--text-shadow);
  }
  .subtitle {
    margin: 28px 60px 0 0;
    font-size: 36px;
    line-height: 50px;
    text-shadow: 2px 3px 4px var(--text-shadow);
  }

  .stars {
    position: absolute;
    left: 0;
    top: 990px;
    width: 900px;
    height: 180px;
  }
</style>
</head>
<body>
  <main class="cover">
    <div class="bands">
      <div class="band band--1"></div>
      <div class="band band--2"></div>
      <div class="band band--3"></div>
      <div class="band band--4"></div>
      <div class="band band--5"></div>
    </div>

    <div class="backdrop-photo" role="img" aria-label="Faint close-up photograph of a broad smile blended into the colour bands"></div>

    <p class="author">Fireman Dale Orsworth</p>

    <header class="title-block">
      <h1 class="title">Standing<br>Growth</h1>
      <p class="subtitle">Keys to Glowing Customer<br>Ratings That Fill The<br>Calendar and Draw Fresh<br>Clients Through Every<br>Entrance!</p>
    </header>

    <svg class="stars" viewBox="0 990 900 180" aria-label="Five star rating">
      <defs>
        <radialGradient id="star-fill" cx="0.45" cy="0.35" r="0.7">
          <stop offset="0" stop-color="var(--star-light)"/>
          <stop offset="0.55" stop-color="var(--star-mid)"/>
          <stop offset="1" stop-color="var(--star-dark)"/>
        </radialGradient>
        <filter id="star-shadow" x="-30%" y="-30%" width="160%" height="160%">
          <feDropShadow dx="3" dy="5" stdDeviation="4" flood-color="#000" flood-opacity="0.4"/>
        </filter>
        <polygon id="star" points="0,-72 17,-23.5 68.5,-22.2 27.6,9 42.3,58.2 0,29 -42.3,58.2 -27.6,9 -68.5,-22.2 -17,-23.5" fill="url(#star-fill)" stroke="#c98412" stroke-width="1.5" stroke-linejoin="round"/>
      </defs>
      <g filter="url(#star-shadow)">
        <use href="#star" x="90" y="1080"/>
        <use href="#star" x="270" y="1080"/>
        <use href="#star" x="450" y="1080"/>
        <use href="#star" x="630" y="1080"/>
        <use href="#star" x="810" y="1080"/>
      </g>
    </svg>
  </main>
</body>
</html>
```